Criação de Papelaria Profissional para Limpeza & Serviço para o lar
" Nossa empresa e familiar, buscamos fazer nosso trabalho com excelencia e qualidade visando o bem estar de nossos clientes. "

```html
<!DOCTYPE html>
<html lang="pt-BR">
<head>
<meta charset="UTF-8">
<title>Assinatura de Email – NestCare Cleaning</title>
<link href="https://fonts.googleapis.com/css2?family=Montserrat:wght@400;500;600;700&display=swap" rel="stylesheet">
<style>
  :root {
    --page-bg: #e4e5e8;
    --card-white: #ffffff;
    --mint: #72d3b6;
    --mint-dark: #3fb896;
    --copper: #c98a45;
    --text-grey: #5b5f63;
    --title-grey: #8a8f94;
  }
  * { margin: 0; padding: 0; box-sizing: border-box; }
  html, body {
    width: 1200px; height: 1200px; overflow: hidden;
    background: var(--page-bg);
    font-family: "Montserrat", sans-serif;
  }
  .canvas {
    width: 1200px; height: 1200px;
    display: flex; align-items: center; justify-content: center;
  }
  .signature {
    position: relative;
    width: 1080px; height: 380px;
    background: var(--card-white);
    border-radius: 14px;
    overflow: hidden;
    box-shadow: 0 14px 40px rgba(0,0,0,0.12);
  }
  .signature-shapes { position: absolute; inset: 0; }
  .accent-bar {
    position: absolute; left: 14px; top: 30px;
    width: 9px; height: 306px;
    background: var(--copper);
  }
  .contact-block {
    position: absolute; left: 56px; top: 38px;
  }
  .person-name {
    font-size: 29px; font-weight: 600; color: var(--mint-dark);
    line-height: 1.1; white-space: nowrap;
  }
  .person-role {
    font-size: 19px; font-weight: 400; color: var(--title-grey);
    margin-top: 2px;
  }
  .contact-list { list-style: none; margin-top: 24px; }
  .contact-item {
    display: flex; align-items: center; gap: 14px;
    font-size: 20px; color: var(--text-grey);
    height: 40px; white-space: nowrap;
  }
  .contact-icon {
    width: 26px; height: 26px; border-radius: 50%;
    background: var(--copper);
    display: flex; align-items: center; justify-content: center;
    flex-shrink: 0;
  }
  .contact-icon svg { width: 14px; height: 14px; }
  .address {
    margin-top: 12px;
    font-size: 19px; line-height: 1.4; color: var(--text-grey);
    white-space: nowrap;
  }
  .brand {
    position: absolute; left: 560px; top: 152px;
    display: flex; align-items: center; gap: 14px;
    white-space: nowrap;
  }
  .brand-dot {
    width: 46px; height: 46px; border-radius: 50%;
    background: var(--copper);
    flex-shrink: 0;
  }
  .brand-name {
    font-size: 34px; font-weight: 700; color: #ffffff;
    letter-spacing: -0.3px;
  }
</style>
</head>
<body>
<main class="canvas">
  <section class="signature">
    <svg class="signature-shapes" viewBox="0 0 1080 380" width="1080" height="380" aria-hidden="true">
      <path class="curve-accent" d="M548 0 L543 40 C512 160 462 280 394 380 L1080 380 L1080 0 Z" fill="var(--copper)"/>
      <path class="mint-panel" d="M548 0 C520 120 472 260 422 380 L1080 380 L1080 0 Z" fill="var(--mint)"/>
    </svg>

    <div class="accent-bar"></div>

    <div class="contact-block">
      <h1 class="person-name">Nome e Sobrenome</h1>
      <p class="person-role">Diretor Comercial</p>
      <ul class="contact-list">
        <li class="contact-item">
          <span class="contact-icon">
            <svg viewBox="0 0 24 24"><path fill="#fff" d="M6.6 10.8a15 15 0 0 0 6.6 6.6l2.2-2.2c.3-.3.7-.4 1-.2 1.1.4 2.3.6 3.6.6.6 0 1 .4 1 1V20c0 .6-.4 1-1 1A17 17 0 0 1 3 4c0-.6.4-1 1-1h3.5c.6 0 1 .4 1 1 0 1.3.2 2.5.6 3.6.1.3 0 .7-.2 1z"/></svg>
          </span>
          (91) 0420-3718
        </li>
        <li class="contact-item">
          <span class="contact-icon">
            <svg viewBox="0 0 24 24"><rect x="3" y="5" width="18" height="14" rx="2" fill="#fff"/><path d="M3.5 6l8.5 7 8.5-7" fill="none" stroke="var(--copper)" stroke-width="2"/></svg>
          </span>
          nestcare@mail.com
        </li>
        <li class="contact-item">
          <span class="contact-icon"></span>
          /nestcare
        </li>
        <li class="contact-item">
          <span class="contact-icon"></span>
          @nestcare
        </li>
      </ul>
      <p class="address">Av. das Acácias, 845 | Centro<br>CEP: 04512-300 | Cidade/UF</p>
    </div>

    <div class="brand">
      <span class="brand-dot"></span>
      <span class="brand-name">NestCare Cleaning</span>
    </div>
  </section>
</main>
</body>
</html>
```